Flyer template design for a builder supply

I need a template for a monthly tool flyer for our builder supply. Something like what the Timber Hollow would put out, but needs to be generic and something I can edit using inexpensive software (ie. MS Publisher) to change things like - product images, prices, descriptions, name of the sale, sale dates, etc.

Attached is a flyer that was made for us by one of our tool suppliers (Brenwick Tool co.) as an example of what we've done in the past. I do not want their logo on it, as this will be used to feature many products that we sell, not just those from Brenwick.

Must have:
Our logo (attached) - if possible should be edited to "Supplies" instead of "Supply"
Our 2 store locations
Time sale is in effect
Our website

Our company supplies products for contractors doing decorative concrete. More info can be found on our website.

```html
<!DOCTYPE html>
<html lang="en">
<head>
<meta charset="utf-8">
<title>Calloway Concrete Supply – Tool Flyer</title>
<link href="https://fonts.googleapis.com/css2?family=Archivo:wght@800&family=PT+Sans+Narrow:wght@700&family=Source+Sans+3:wght@400;600;700&display=swap" rel="stylesheet">
<style>
  :root {
    --blue: #1f6fb5;
    --blue-light: #5d9fd8;
    --navy: #2b2f4a;
    --navy-dark: #1d2033;
    --ink: #111111;
    --paper: #eeeff1;
    --card: #ffffff;
    --fold: #c9ccd3;
  }
  * { box-sizing: border-box; margin: 0; padding: 0; }
  html, body { width: 946px; height: 1200px; overflow: hidden; background: var(--paper); }
  body { font-family: "Source Sans 3", Arial, sans-serif; color: var(--ink); }

  .flyer { position: relative; width: 946px; height: 1200px; background: var(--paper); }

  .header { position: absolute; left: 0; top: 0; width: 946px; height: 164px; }
  .brand { position: absolute; left: 28px; top: 40px; }
  .brand-line { display: flex; align-items: center; gap: 8px; }
  .brand-mark { width: 18px; height: 18px; background: var(--blue); }
  .brand-name { font-family: "Archivo", Arial, sans-serif; font-weight: 800; font-size: 46px; color: var(--blue); letter-spacing: 1px; line-height: 1; }
  .brand-tag { margin-top: 6px; margin-left: 26px; font-size: 19px; letter-spacing: 3px; color: var(--ink); border-bottom: 2px solid var(--ink); padding-bottom: 2px; display: inline-block; }

  .sale-dates { position: absolute; left: 346px; top: 30px; width: 420px; text-align: center; font-family: "Archivo", Arial, sans-serif; font-weight: 800; line-height: 1.05; }
  .sale-dates .label { font-size: 29px; color: var(--ink); margin-bottom: 4px; }
  .sale-dates .range { font-size: 38px; color: var(--blue); }
  .sale-dates sup { font-size: 0.55em; vertical-align: 0.7em; }

  .rule { position: absolute; left: 0; top: 164px; width: 946px; height: 11px; background: var(--ink); }
  .rule-shade { position: absolute; left: 0; top: 175px; width: 946px; height: 14px; background: linear-gradient(#d6d8dc, var(--paper)); }

  .fold { position: absolute; left: 473px; top: 0; width: 1px; height: 1200px; background: var(--fold); }

  .card { position: absolute; width: 462px; height: 202px; background: var(--card); box-shadow: 0 2px 6px rgba(0,0,0,0.12); }
  .card.left { left: 0; }
  .card.right { left: 484px; }
  .row1 { top: 200px; } .row2 { top: 416px; } .row3 { top: 632px; } .row4 { top: 848px; }

  .product-img { position: absolute; left: 16px; top: 40px; width: 244px; height: 130px; border-radius: 6px; }
  .img-float-orange { background: linear-gradient(160deg, #ffffff 10%, #e6792f 45%, #b8bcc6 70%, #ffffff); }
  .img-float-wood { background: linear-gradient(160deg, #ffffff 10%, #d9b98c 45%, #a9adbd 70%, #ffffff); }
  .img-trowel { background: linear-gradient(160deg, #ffffff 15%, #d8dadd 50%, #c9b48c 60%, #ffffff); }
  .img-placer { background: linear-gradient(200deg, #ffffff 15%, #2d8bb0 40%, #b9bcc1 75%, #ffffff); }
  .img-groover { background: linear-gradient(160deg, #ffffff 10%, #c6c9ce 50%, #ffffff); }
  .img-bar { background: linear-gradient(180deg, #ffffff 40%, #8d9095 50%, #ffffff 60%); }
  .img-broom { background: linear-gradient(180deg, #ffffff 25%, #dfe1e4 40%, #1f1f1f 55%, #1f1f1f 70%, #ffffff 80%); }
  .img-edger { background: linear-gradient(160deg, #ffffff 10%, #c2c5ca 50%, #ffffff); }

  .product-info { position: absolute; right: 16px; top: 10px; text-align: right; }
  .product-name { font-family: "PT Sans Narrow", Arial, sans-serif; font-weight: 700; font-size: 20px; line-height: 1.2; color: var(--blue); }
  .product-size { font-size: 17px; line-height: 1.3; color: var(--ink); }

  .price { position: absolute; right: 16px; bottom: 17px; min-width: 140px; height: 38px; padding: 0 12px; border-radius: 7px; display: flex; align-items: center; justify-content: center; font-size: 18px; color: #ffffff; box-shadow: 0 3px 0 rgba(0,0,0,0.25); }
  .price.dark { background: linear-gradient(#4a4f6f, var(--navy) 55%, var(--navy-dark)); }
  .price.blue { background: linear-gradient(#86bbe6, var(--blue-light) 55%, var(--blue)); }

  .footer { position: absolute; left: 0; top: 1050px; width: 946px; height: 150px; }
  .store { position: absolute; top: 20px; font-size: 17px; line-height: 1.62; color: #333333; }
  .store .city { font-weight: 700; color: var(--blue); font-size: 17px; }
  .store.first { left: 18px; }
  .store.second { left: 205px; }
  .tagline { position: absolute; left: 489px; top: 24px; font-family: "PT Sans Narrow", Arial, sans-serif; font-weight: 700; font-size: 29px; line-height: 1.32; color: var(--blue); }
  .website { position: absolute; left: 493px; top: 112px; font-size: 20px; color: #222222; letter-spacing: 0.3px; }
</style>
</head>
<body>
<div class="flyer">
  <div class="fold"></div>

  <header class="header">
    <div class="brand">
      <div class="brand-line">
        <span class="brand-mark"></span>
        <span class="brand-name">CALLOWAY</span>
      </div>
      <span class="brand-tag">CONCRETE SUPPLY</span>
    </div>
    <div class="sale-dates">
      <div class="label">Pricing effective :</div>
      <div class="range">1<sup>st</sup> March to</div>
      <div class="range">30<sup>th</sup> April 2014</div>
    </div>
  </header>
  <div class="rule"></div>
  <div class="rule-shade"></div>

  <section class="card left row1">
    <div class="product-img img-float-orange" role="img" aria-label="Magnesium hand float with orange grip handle"></div>
    <div class="product-info">
      <div class="product-name">Magnesium Hand Float<br>w/GripForm® Handle</div>
      <div class="product-size">12”x3-1/4”</div>
    </div>
    <div class="price dark">HF1203G - $23.00</div>
  </section>

  <section class="card right row1">
    <div class="product-img img-float-wood" role="img" aria-label="Round end magnesium hand float with wooden handle"></div>
    <div class="product-info">
      <div class="product-name">Round End Magnesium<br>Hand Float w/High Lift</div>
      <div class="product-size">20”X3-1/4”</div>
    </div>
    <div class="price blue">HF2031 - $28.00</div>
  </section>

  <section class="card left row2">
    <div class="product-img img-trowel" role="img" aria-label="Cement trowel with straight wood handle"></div>
    <div class="product-info">
      <div class="product-name">Cement Trowel w/<br>Straight Wood Handle</div>
      <div class="product-size">10”x4”</div>
    </div>
    <div class="price blue">TR1044 - $26.50</div>
  </section>

  <section class="card right row2">
    <div class="product-img img-placer" role="img" aria-label="Right angle concrete placer with blue pole"></div>
    <div class="product-info">
      <div class="product-name">Right Angle Concrete<br>Placer W/ Hook</div>
      <div class="product-size">19-1/2”x4”</div>
    </div>
    <div class="price dark">PL1954 - $29.10</div>
  </section>

  <section class="card left row3">
    <div class="product-img img-groover" role="img" aria-label="Airplane groover with tilt bracket"></div>
    <div class="product-info">
      <div class="product-name">Airplane Groover<br>w/EasyAngle® II Bracket</div>
      <div class="product-size">24”x8” Radius</div>
    </div>
    <div class="price dark">GR2408A - $158.00</div>
  </section>

  <section class="card right row3">
    <div class="product-img img-bar" role="img" aria-label="Square end carbon steel blade"></div>
    <div class="product-info">
      <div class="product-name">Square End<br>Carbon Steel</div>
      <div class="product-size">5”x18</div>
    </div>
    <div class="price blue">SE0518 - $32.00</div>
  </section>

  <section class="card left row4">
    <div class="product-img img-broom" role="img" aria-label="Aluminium cement finish broom head"></div>
    <div class="product-info">
      <div class="product-name">Alum Med Cement<br>Finish Broom</div>
      <div class="product-size">24”</div>
    </div>
    <div class="price blue">BR2400 - $62.50</div>
  </section>

  <section class="card right row4">
    <div class="product-img img-edger" role="img" aria-label="Walking seamer edger with handle socket"></div>
    <div class="product-info">
      <div class="product-name">Walking Seamer/<br>edger</div>
      <div class="product-size">8”x 8”, 1/4” Radius</div>
    </div>
    <div class="price dark">SM0808 - $49.50</div>
  </section>

  <footer class="footer">
    <div class="store first">
      <div class="city">Harborview Location,</div>
      <div>412 Marlow Ave. N.</div>
      <div>Phone: 555 014 2088</div>
      <div>Fax: 555 014 2089</div>
    </div>
    <div class="store second">
      <div class="city">Ashford Location,</div>
      <div>86 Kestrel Blvd. Unit 7</div>
      <div>Phone: 555 018 3144</div>
      <div>Fax: 555 018 7289</div>
    </div>
    <div class="tagline">For all your exposed and stamped<br>concrete needs!</div>
    <div class="website">www.callowayconcrete.com</div>
  </footer>
</div>
</body>
</html>
```